Brochure for a Laundry

We need a Brochure Designed for a the Harbor Wash (www.theharborwash-example.com)
A SAMPLE BROCHURE by the Owner of the Brand is also attached for complete review. We need something along the same lines.

Please see the DROPBOX Link below to access the complete Content including written content, pictures, Sample Brochure etc
DROPBOX LINK:
https://www.filestash-example.com/sh/qpwetrbzunxvk/BBF-TelnoAQc7xKPzWsUvG4ko?dl=0

```html
<!DOCTYPE html>
<html lang="en">
<head>
<meta charset="utf-8">
<title>The Harbor Wash — Brochure</title>
<link href="https://fonts.googleapis.com/css2?family=Open+Sans:wght@400;600;700&display=swap" rel="stylesheet">
<style>
  :root{
    --bg:#d9dcdf;
    --paper:#ffffff;
    --pink:#e6007a;
    --pink-soft:#f7c9de;
    --ink:#111111;
    --text:#333333;
    --grey:#8a8a8a;
  }
  *{box-sizing:border-box;margin:0;padding:0}
  html,body{width:1200px;height:852px;overflow:hidden;background:var(--bg);font-family:"Open Sans",Arial,sans-serif}
  .sheet{position:relative;width:1200px;height:852px}
  .page{position:absolute;width:560px;height:396px;background:var(--paper);overflow:hidden;box-shadow:0 2px 8px rgba(0,0,0,.15)}
  .back-cover{left:30px;top:20px}
  .front-cover{left:610px;top:20px}
  .spread-left{left:30px;top:436px}
  .spread-right{left:610px;top:436px}
  .page svg.bg{position:absolute;inset:0;width:100%;height:100%}
  .brand{font-weight:700;color:var(--pink);font-size:26px;letter-spacing:.5px;display:flex;align-items:center;gap:8px;white-space:nowrap}
  .brand .dot{width:10px;height:10px;border-radius:50%;background:var(--pink)}
  .back-cover .brand{position:absolute;left:28px;top:228px}
  .back-cover .pitch{position:absolute;left:28px;top:272px;width:300px;font-size:12px;color:var(--ink);line-height:1.45}
  .contact{position:absolute;left:28px;top:318px;list-style:none;font-size:11px;color:var(--ink);line-height:1.75}
  .contact li{display:flex;align-items:center;gap:7px}
  .contact svg{width:11px;height:11px;fill:var(--pink)}
  .front-cover .suit{position:absolute;left:140px;top:20px;width:300px;height:300px;border-radius:50%;background:radial-gradient(circle at 50% 40%,#3a3a3a,#050505 70%)}
  .front-cover .brand{position:absolute;left:24px;top:248px;font-size:24px}
  .photo{position:absolute;inset:0;background:linear-gradient(160deg,#4a4a4a 0%,#1a1a1a 45%,#c2366e 70%,#c9772e 100%)}
  .spread-right .body{position:absolute;left:150px;top:22px;width:388px;font-size:8.4px;line-height:1.36;color:var(--text)}
  .body p{margin-bottom:6px}
  .body ul{list-style:none;margin:3px 0 6px 24px;font-weight:700;color:var(--ink)}
  .spread-right .brand{position:absolute;right:22px;bottom:10px;font-size:18px}
</style>
</head>
<body>
<main class="sheet">

  <section class="page back-cover">
    <svg class="bg" viewBox="0 0 560 396" preserveAspectRatio="none" aria-hidden="true">
      <defs>
        <linearGradient id="fade" x1="0" y1="1" x2="1" y2="0">
          <stop offset="0" stop-color="#f6bcd6"/>
          <stop offset=".55" stop-color="#ffffff"/>
        </linearGradient>
      </defs>
      <rect width="560" height="396" fill="url(#fade)"/>
    </svg>
    <div class="brand"><span class="dot"></span>THE HARBOR WASH</div>
    <p class="pitch">Are you ready to open a profitable Harbor Wash store? Call us for more details today.</p>
    <ul class="contact">
      <li><svg viewBox="0 0 24 24"><path d="M6.6 10.8a15 15 0 0 0 6.6 6.6l2.2-2.2a1 1 0 0 1 1-.25 11 11 0 0 0 3.6.6 1 1 0 0 1 1 1V20a1 1 0 0 1-1 1A17 17 0 0 1 3 4a1 1 0 0 1 1-1h3.5a1 1 0 0 1 1 1 11 11 0 0 0 .6 3.6 1 1 0 0 1-.25 1z"/></svg>+91 90000 12345</li>
      <li><svg viewBox="0 0 24 24"><circle cx="12" cy="12" r="10"/></svg>www.theharborwash-example.com</li>
      <li><svg viewBox="0 0 24 24"><path d="M12 2a7 7 0 0 0-7 7c0 5 7 13 7 13s7-8 7-13a7 7 0 0 0-7-7zm0 9.5A2.5 2.5 0 1 1 12 6.5a2.5 2.5 0 0 1 0 5z"/></svg>Kolkata &nbsp;·&nbsp; Navi-Mumbai</li>
    </ul>
  </section>

  <section class="page front-cover">
    <svg class="bg" viewBox="0 0 560 396" preserveAspectRatio="none" aria-hidden="true">
      <rect width="560" height="396" fill="#ffffff"/>
      <path d="M0 60 Q280 -60 560 70 L560 396 L0 396 Z" fill="var(--pink)"/>
      <path d="M0 120 Q280 -20 560 120 L560 330 Q280 430 0 300 Z" fill="var(--ink)"/>
    </svg>
    <div class="suit" role="img" aria-label="Photo of a dark suit with white shirt and pink tie"></div>
    <div class="brand"><span class="dot"></span>THE HARBOR WASH</div>
  </section>

  <section class="page spread-left">
    <div class="photo" role="img" aria-label="Photo of a bride in an embroidered pink and gold lehenga against a dark room"></div>
  </section>

  <section class="page spread-right">
    <svg class="bg" viewBox="0 0 560 396" preserveAspectRatio="none" aria-hidden="true">
      <rect width="560" height="396" fill="#ffffff"/>
      <path d="M0 0 L110 0 Q150 200 130 396 L0 396 Z" fill="#0c0c0c"/>
    </svg>
    <div class="body">
      <p>The Harbor Wash is a premium fashion dry cleaner servicing all of India. We are based in Navi-Mumbai and provide high quality and professional services to the fashion industry. A number of fashion designers depend on us due to our commitment to excellence and we continue to strive to meet and exceed client expectations.</p>
      <p>We are unique in that we service the fashion industry exclusively. We use European machines with Green Eco-Friendly Technology and detergents and take an 8 step approach to our services to guarantee you the highest possible quality.</p>
      <p>Learn more to find out why The Harbor Wash has become the trusted laundry provider for fashion designers and commercial clients alike, all throughout India.</p>
      <p>As a professional laundry service to the fashion industry, we have a strong understanding of the various garment materials. At The Harbor Wash, we work with the fashion designers to learn about the materials and how to treat them with the utmost respect. This makes a difference and we pride ourselves on the level of care that we take when laundering the various garments that are brought to us.</p>
      <p>Due to our work across India, we have become associated with some of the most iconic names throughout the fashion industry. This includes such as Marlo Vestri, Anika Roy, Colm Weston, Bellardi, Aneesha Dev, Vikram Kaul, Sunil Dasmal, and many more.</p>
      <p>Services we offer include:</p>
      <ul>
        <li>- Dry cleaning</li>
        <li>- Laundry services</li>
        <li>- Ornamental garments</li>
      </ul>
      <p>Step into a fashion boutique and find out who provides their laundry and dry cleaning services. If it is done right, they will proudly say The Harbor Wash.</p>
    </div>
    <div class="brand"><span class="dot"></span>THE HARBOR WASH</div>
  </section>

</main>
</body>
</html>
```